Business Card Design

I would like a new business card for my business Drive Haven, we operate within the automotive industry and offer customer retention solutions for independent mechanical workshops across Australia and New Zealand. The program incorporates service reminders and roadside assistance for consumers and is designed to get the client back for their vehicle service visit, I would like a doubled sided design that incorporates my logos and a two tone type card that has white and a carbon fibre look also use the blue in the logo I have uploaded. It would be great to have icons as the phone/fax/email etc details for the card are below. The finished design must be a print ready file useable.It would be great if the design could communicate the what type of business we are
Marcus Trelby
General Manager
Drive Haven Pty Ltd
Unit 5/42 Corrin Street
Wexmoor Newcastle NSW 2391
Ph:+61240173500
fax:+61240173600
Mobile:0415889214
Email:info@drivehaven-example.com.au
Updates
I have just upload a carbon fibre background for the business card hope it helps
Hello guys I am sorry fr no feedback I have been away over seas I will send feedback when I return monday
Industry/Entity Type
Automotive
Look and feel

```html
<!DOCTYPE html>
<html lang="en">
<head>
<meta charset="utf-8">
<title>Drive Haven – Business Card</title>
<link href="https://fonts.googleapis.com/css2?family=Open+Sans:wght@400;600;700&display=swap" rel="stylesheet">
<style>
  :root {
    --backdrop: #e6e6e6;
    --carbon-dark: #141414;
    --carbon-mid: #2b2b2b;
    --band-white: #f4f4f4;
    --brand-blue: #1ea0dc;
    --ink-grey: #5a5a5a;
    --muted-grey: #a3a3a3;
    --text-white: #f2f2f2;
  }
  * { box-sizing: border-box; margin: 0; padding: 0; }
  html, body { width: 1200px; height: 800px; overflow: hidden; }
  body {
    background: var(--backdrop);
    font-family: "Open Sans", Arial, sans-serif;
    display: flex;
    align-items: center;
    justify-content: center;
    gap: 60px;
  }
  .card {
    position: relative;
    width: 520px;
    height: 300px;
    border-radius: 3px;
    overflow: hidden;
    box-shadow: 0 6px 18px rgba(0,0,0,0.18);
  }
  .carbon-surface {
    position: absolute;
    inset: 0;
    background: radial-gradient(ellipse at 40% 35%, var(--carbon-mid), var(--carbon-dark) 75%);
  }

  /* Front */
  .brand-band {
    position: absolute;
    left: 40px;
    top: 100px;
    width: 450px;
    height: 100px;
    background: var(--band-white);
    display: flex;
    align-items: center;
    padding-left: 28px;
    gap: 22px;
  }
  .brand-dot {
    width: 62px;
    height: 62px;
    border-radius: 50%;
    background: var(--brand-blue);
    flex: none;
  }
  .brand-name {
    font-weight: 700;
    font-size: 46px;
    color: var(--ink-grey);
    letter-spacing: 0.5px;
  }

  /* Back */
  .brand-badge {
    position: absolute;
    left: 24px;
    top: 24px;
    width: 190px;
    height: 48px;
    background: var(--band-white);
    display: flex;
    align-items: center;
    padding-left: 10px;
    gap: 10px;
  }
  .brand-badge .brand-dot { width: 32px; height: 32px; }
  .brand-badge .brand-name { font-size: 20px; }

  .company-address {
    position: absolute;
    left: 24px;
    top: 100px;
    font-size: 11.5px;
    line-height: 1.45;
    color: var(--muted-grey);
  }

  .contact-block {
    position: absolute;
    left: 262px;
    top: 138px;
  }
  .person-name {
    font-weight: 700;
    font-size: 18px;
    letter-spacing: 0.6px;
    color: var(--brand-blue);
    text-transform: uppercase;
  }
  .person-role {
    font-size: 12.5px;
    letter-spacing: 0.6px;
    color: var(--text-white);
    text-transform: uppercase;
    margin-bottom: 8px;
  }
  .contact-list {
    list-style: none;
    border-left: 2px solid var(--brand-blue);
    padding-left: 10px;
    margin-left: -14px;
  }
  .contact-list li {
    display: flex;
    align-items: center;
    gap: 10px;
    font-size: 11.5px;
    line-height: 20px;
    color: var(--text-white);
  }
  .contact-icon { width: 11px; height: 11px; fill: var(--text-white); flex: none; }
</style>
</head>
<body>

  <section class="card card-front" aria-label="Business card front">
    <div class="carbon-surface" role="img" aria-label="Carbon fibre texture background"></div>
    <div class="brand-band">
      <span class="brand-dot"></span>
      <span class="brand-name">Drive Haven</span>
    </div>
  </section>

  <section class="card card-back" aria-label="Business card back">
    <div class="carbon-surface" role="img" aria-label="Carbon fibre texture background"></div>

    <div class="brand-badge">
      <span class="brand-dot"></span>
      <span class="brand-name">Drive Haven</span>
    </div>

    <address class="company-address">
      Drive Haven Pty Ltd<br>
      Unit 5/42 Corrin Street<br>
      Wexmoor Newcastle<br>
      NSW 2391
    </address>

    <div class="contact-block">
      <p class="person-name">Marcus Trelby</p>
      <p class="person-role">General Manager</p>
      <ul class="contact-list">
        <li>
          <svg class="contact-icon" viewBox="0 0 24 24" aria-hidden="true"><path d="M6.6 10.8a15.1 15.1 0 0 0 6.6 6.6l2.2-2.2a1 1 0 0 1 1-.25 11.4 11.4 0 0 0 3.6.57 1 1 0 0 1 1 1V20a1 1 0 0 1-1 1A17 17 0 0 1 3 4a1 1 0 0 1 1-1h3.5a1 1 0 0 1 1 1c0 1.25.2 2.45.57 3.57a1 1 0 0 1-.25 1z"/></svg>
          +61240173500
        </li>
        <li>
          <svg class="contact-icon" viewBox="0 0 24 24" aria-hidden="true"><path d="M6 2h9v5h3v15H6zM3 9h2v11H3zM9 11h6v2H9zm0 4h6v2H9z"/></svg>
          +61240173600
        </li>
        <li>
          <svg class="contact-icon" viewBox="0 0 24 24" aria-hidden="true"><path d="M7 1h10a2 2 0 0 1 2 2v18a2 2 0 0 1-2 2H7a2 2 0 0 1-2-2V3a2 2 0 0 1 2-2zm0 3v14h10V4zm5 15.5a1 1 0 1 0 0 2 1 1 0 0 0 0-2z"/></svg>
          0415889214
        </li>
        <li>
          <svg class="contact-icon" viewBox="0 0 24 24" aria-hidden="true"><path d="M2 5h20v14H2zm2 2v.5l8 5 8-5V7zm0 2.9V17h16V9.9l-8 5z"/></svg>
          info@drivehaven-example.com.au
        </li>
      </ul>
    </div>
  </section>

</body>
</html>
```